Massage Therapy and Personal Training Business Card (Lorvex Wellness)

I need a logo design based in Washington. The company is called Lorvex Wellness. Lorvex are my initials. I specialize in massage therapy and personal training and general wellness of my clients. I've tried getting designs but haven't quite yet found what I'm looking for. I'm not inclined to a certain color yet but some color that resembles wellness such as light blue and white or green and white. Again, I'm not really picky about that. Thank you in advance

Industry/Entity Type

Business

Contact Information for Business Card

Have the description on one side and space for writing information on the back side such as number, appt, etc. I have an example attached. I see a lot of these card. I dont want the exact one, but something similar. Simple, professional and elegant.

Colors

Designer to choose colors to be used in the design.

Requirements
Must have
• Space on the back side to write
• A professional, elegant look
Should not have
• cartoon like style.

```html
<!DOCTYPE html>
<html lang="en">
<head>
<meta charset="utf-8">
<title>Lorvex Wellness – Business Card</title>
<link rel="stylesheet" href="https://fonts.googleapis.com/css2?family=Roboto:wght@300;400;500&display=swap">
<style>
  :root {
    --bg: #e9ecef;
    --card-white: #f4f6f8;
    --card-white-edge: #dde2e7;
    --ink-blue: #2f5a86;
    --ink-soft: #5f7f9f;
    --write-line: #a9b9ca;
    --sea-deep: #2d5f93;
    --sea-mid: #3f86bf;
    --sea-light: #5cb0dc;
    --shore-green: #4f9a9a;
    --white: #ffffff;
  }
  * { box-sizing: border-box; margin: 0; padding: 0; }
  html, body { width: 1200px; height: 800px; overflow: hidden; }
  body {
    background: var(--bg);
    font-family: "Roboto", Arial, sans-serif;
    position: relative;
  }
  .card {
    position: absolute;
    top: 245px;
    width: 540px;
    height: 309px;
    border-radius: 4px;
    overflow: hidden;
    box-shadow: 0 10px 30px rgba(30, 50, 70, 0.18);
  }

  /* Back side: contact details and writing space */
  .card--back {
    left: 40px;
    background: linear-gradient(160deg, var(--card-white) 0%, var(--card-white-edge) 100%);
  }
  .leaf-scatter {
    position: absolute;
    left: 0; bottom: 0;
    width: 200px; height: 170px;
    background: radial-gradient(ellipse at 40% 60%, rgba(138,160,184,0.35) 0%, rgba(138,160,184,0) 70%);
  }
  .holder {
    position: absolute;
    left: 34px; top: 28px;
    color: var(--ink-blue);
  }
  .holder__name {
    font-size: 40px;
    font-weight: 500;
    letter-spacing: -0.5px;
    line-height: 1;
  }
  .holder__role {
    font-size: 17px;
    font-weight: 400;
    color: var(--ink-soft);
    margin-top: 4px;
    margin-left: 60px;
  }
  .contact-list {
    position: absolute;
    left: 210px; top: 94px;
    list-style: none;
    color: var(--ink-blue);
  }
  .contact-list li {
    display: flex;
    align-items: center;
    height: 29px;
    font-size: 16px;
    white-space: nowrap;
  }
  .contact-list li.contact--address { font-size: 12px; color: var(--ink-soft); }
  .contact-list svg { width: 21px; height: 21px; margin-right: 12px; flex: none; }
  .write-space {
    position: absolute;
    left: 210px; right: 34px; top: 248px;
  }
  .write-space__line {
    height: 26px;
    border-bottom: 1px solid var(--write-line);
  }

  /* Front side: brand */
  .card--front {
    left: 620px;
    background: linear-gradient(170deg, var(--sea-deep) 0%, var(--sea-mid) 45%, var(--sea-light) 75%, var(--shore-green) 100%);
  }
  .scene {
    position: absolute; inset: 0;
    background:
      linear-gradient(180deg, rgba(255,255,255,0.10) 0%, rgba(255,255,255,0) 40%),
      radial-gradient(ellipse at 75% 85%, rgba(90,170,120,0.45) 0%, rgba(90,170,120,0) 55%);
  }
  .brand {
    position: absolute;
    left: 44px; bottom: 58px;
    color: var(--white);
  }
  .brand__name {
    font-size: 58px;
    font-weight: 400;
    line-height: 1;
    letter-spacing: 0.5px;
  }
  .brand__tagline {
    font-size: 19px;
    font-weight: 500;
    line-height: 1.25;
    margin-top: 10px;
    margin-left: 40px;
  }
</style>
</head>
<body>

<section class="card card--back" aria-label="Card back – contact details and writing space">
  <div class="leaf-scatter" role="img" aria-label="Scattered soft blue leaves drifting across the corner"></div>
  <div class="holder">
    <p class="holder__name">Your Name</p>
    <p class="holder__role">Job Role</p>
  </div>
  <ul class="contact-list">
    <li class="contact--address">
      <svg viewBox="0 0 24 24" aria-hidden="true"><circle cx="12" cy="12" r="11" fill="none" stroke="#2f5a86" stroke-width="1.5"/><path d="M12 6a4 4 0 0 0-4 4c0 3 4 8 4 8s4-5 4-8a4 4 0 0 0-4-4z" fill="#2f5a86"/><circle cx="12" cy="10" r="1.5" fill="#f4f6f8"/></svg>
      Street Address 1480 Harbor View Rd
    </li>
    <li>
      <svg viewBox="0 0 24 24" aria-hidden="true"><circle cx="12" cy="12" r="11" fill="none" stroke="#2f5a86" stroke-width="1.5"/><path d="M8.5 7l2 2.5-1.2 1.4a7 7 0 0 0 3.8 3.8l1.4-1.2 2.5 2-1.3 1.6c-4 0-8.5-4.5-8.5-8.5z" fill="#2f5a86"/></svg>
      044 615 20 00
    </li>
    <li>
      <svg viewBox="0 0 24 24" aria-hidden="true"><circle cx="12" cy="12" r="11" fill="#2f5a86"/><rect x="8" y="6.5" width="8" height="4" fill="#f4f6f8"/><rect x="6.5" y="10.5" width="11" height="5" rx="1" fill="#f4f6f8"/><rect x="8.5" y="14" width="7" height="3.5" fill="#2f5a86" stroke="#f4f6f8"/></svg>
      044 615 20 01
    </li>
    <li>
      <svg viewBox="0 0 24 24" aria-hidden="true"><circle cx="12" cy="12" r="11" fill="#2f5a86"/><rect x="6.5" y="8" width="11" height="8" fill="#f4f6f8"/><path d="M6.5 8l5.5 4.5L17.5 8" fill="none" stroke="#2f5a86" stroke-width="1.2"/></svg>
      contact@lorvexwellness.com
    </li>
    <li>
      <svg viewBox="0 0 24 24" aria-hidden="true"><circle cx="12" cy="12" r="11" fill="#2f5a86"/><circle cx="12" cy="12" r="6" fill="none" stroke="#f4f6f8" stroke-width="1.2"/><ellipse cx="12" cy="12" rx="2.6" ry="6" fill="none" stroke="#f4f6f8" stroke-width="1.2"/><path d="M6 12h12" stroke="#f4f6f8" stroke-width="1.2"/></svg>
      www.lorvexwellness.com
    </li>
  </ul>
  <div class="write-space" aria-label="Blank lines for writing appointments">
    <div class="write-space__line"></div>
    <div class="write-space__line"></div>
  </div>
</section>

<section class="card card--front" aria-label="Card front – brand">
  <div class="scene" role="img" aria-label="Misty blue lake landscape with trees and a green shoreline"></div>
  <div class="brand">
    <h1 class="brand__name">Lorvex Wellness</h1>
    <p class="brand__tagline">massage therapy and personal training<br>and general wellness</p>
  </div>
</section>

</body>
</html>
```